Nu-Disco track "Keep Turning Around" CD artwork.

Need cover art for the single entitled:
'Keep Turning Around'
Band: GlowPavlane
https://www.glimmerbook.example/pages/GlowPavlane/581036294417853
Here's the track:
http://tnq.example/48PzRuK
CD cover Inspiration for these disco inspired track is original LP art from Velvet Orbit Parade. GlowPavlane in place of VOP at top, include a disco ball, track title.
I'm envisioning "hipsters" dancing on the dancefloor....
Design will need to incorporate standard elements from the Brightmoor Platter label (PSD included)
Updates
Please READ the design brief. Otherwise what's the point of me writing it.
Artwork needs EP added at the end of the song title. "Keep Turning Around EP"
Hi folks.....song title has been shortened to make layouts easier. Eliminate "IT" from title. Title now "Keep Turning Round"
Reminder....the title is "Keep Turning Round EP"

```html
<!DOCTYPE html>
<html lang="en">
<head>
<meta charset="utf-8">
<title>GlowPavlane – Keep Turning Round EP cover</title>
<link rel="stylesheet" href="https://fonts.googleapis.com/css2?family=Audiowide&family=Lobster&display=swap">
<style>
  :root {
    --page-bg: #e4e4e4;
    --edge-white: #ffffff;
    --frame-black: #05060a;
    --frame-cyan: #2a8fb0;
    --frame-light: #d9f2fa;
    --club-purple: #5a1f8a;
    --club-pink: #e0379f;
    --club-red: #c8283f;
    --club-blue: #1d3f9a;
    --club-dark: #0a0616;
    --ball-light: #f4f6ff;
    --ball-mid: #aeb6e6;
    --ball-dark: #5d5fa8;
    --chrome-light: #ffffff;
    --chrome-mid: #b9bec8;
    --chrome-dark: #5b6170;
    --title-pink: #ff2f86;
    --title-yellow: #ffe03a;
    --label-cyan: #2aa6c9;
    --label-ink: #0b0b0f;
  }
  * { margin: 0; padding: 0; box-sizing: border-box; }
  html, body { width: 1200px; height: 848px; overflow: hidden; }
  body { background: var(--page-bg); position: relative; }

  .cover {
    position: absolute; left: 249px; top: 38px;
    width: 702px; height: 702px;
    background: var(--frame-black);
    border: 5px solid var(--edge-white);
    box-shadow: 0 3px 10px rgba(0,0,0,.35);
    overflow: hidden;
  }
  .frame-lines {
    position: absolute; inset: 18px;
    border: 3px solid var(--frame-cyan);
    box-shadow: inset 0 0 0 4px var(--frame-light), inset 0 0 0 8px var(--frame-black), inset 0 0 0 11px var(--frame-cyan);
  }
  .club-scene {
    position: absolute; inset: 40px; overflow: hidden;
    background:
      radial-gradient(ellipse at 50% 30%, rgba(255,120,200,.55) 0, transparent 50%),
      radial-gradient(ellipse at 18% 45%, rgba(200,40,63,.7) 0, transparent 40%),
      radial-gradient(ellipse at 82% 45%, rgba(200,40,63,.6) 0, transparent 40%),
      radial-gradient(ellipse at 20% 20%, var(--club-blue) 0, transparent 45%),
      radial-gradient(ellipse at 85% 20%, var(--club-purple) 0, transparent 45%),
      linear-gradient(180deg, #1a0b3a 0%, var(--club-purple) 45%, var(--club-dark) 100%);
  }
  .light-beams {
    position: absolute; left: 50%; top: 100px; width: 900px; height: 900px;
    margin-left: -450px; margin-top: -450px;
    background: conic-gradient(from 90deg,
      transparent 0deg, rgba(255,90,160,.35) 10deg, transparent 20deg,
      rgba(255,70,110,.3) 35deg, transparent 45deg, rgba(230,120,255,.3) 60deg, transparent 72deg,
      rgba(255,120,200,.35) 88deg, transparent 100deg, rgba(255,70,110,.3) 118deg, transparent 130deg,
      rgba(255,90,160,.35) 150deg, transparent 165deg, transparent 360deg);
  }
  .disco-ball {
    position: absolute; left: 232px; top: 30px;
    width: 220px; height: 220px; border-radius: 50%;
    background:
      radial-gradient(circle at 38% 40%, var(--ball-light) 0, rgba(244,246,255,.85) 18%, transparent 42%),
      radial-gradient(circle at 50% 50%, var(--ball-mid) 0, var(--ball-dark) 75%, #3a2d70 100%);
    box-shadow: 0 0 60px 20px rgba(210,190,255,.45);
  }
  .dancer {
    position: absolute; left: 250px; top: 190px; width: 130px; height: 450px;
    border-radius: 60px 60px 20px 20px;
    background: linear-gradient(180deg, rgba(255,200,220,.75) 0%, rgba(240,110,190,.7) 45%, rgba(120,40,110,.5) 100%);
    filter: blur(6px);
  }
  .crowd {
    position: absolute; left: 0; right: 0; bottom: 0; height: 330px;
    background:
      linear-gradient(180deg, transparent 0%, rgba(60,20,110,.75) 25%, rgba(25,8,45,.95) 70%, #0d0618 100%);
  }
  .dance-floor {
    position: absolute; left: 40px; right: 40px; bottom: 0; height: 150px;
    background: radial-gradient(ellipse at 50% 60%, rgba(255,90,120,.45) 0, rgba(120,80,200,.25) 45%, transparent 75%);
  }
  .band-name {
    position: absolute; left: 0; right: 0; top: 182px;
    text-align: center;
    font-family: "Audiowide", sans-serif; font-weight: 400;
    font-size: 60px; letter-spacing: 1px; text-transform: uppercase;
    background: linear-gradient(180deg, var(--chrome-light) 0%, var(--chrome-mid) 45%, var(--chrome-dark) 55%, var(--chrome-light) 100%);
    -webkit-background-clip: text; background-clip: text; color: transparent;
    filter: drop-shadow(0 2px 2px rgba(0,0,0,.9));
  }
  .release-title {
    position: absolute; left: 50px; top: 408px; width: 600px;
    text-align: center;
    font-family: "Lobster", cursive; font-weight: 400;
    font-size: 64px; line-height: 1;
    color: var(--title-pink);
    -webkit-text-stroke: 2px var(--title-yellow);
    text-shadow: 0 0 10px rgba(255,224,58,.7), 0 3px 4px rgba(0,0,0,.8);
    transform: rotate(-4deg);
  }
  .release-format {
    position: absolute; left: 525px; top: 462px;
    font-family: "Audiowide", sans-serif; font-weight: 400;
    font-size: 44px; font-style: italic; line-height: 1;
    background: linear-gradient(180deg, var(--chrome-light) 0%, var(--chrome-mid) 50%, var(--chrome-dark) 100%);
    -webkit-background-clip: text; background-clip: text; color: transparent;
    filter: drop-shadow(0 2px 2px rgba(0,0,0,.9));
    z-index: 2;
  }
  .facet-shape { position: absolute; left: 462px; top: 490px; width: 180px; height: 150px; }
  .label-mark {
    position: absolute; left: 54px; top: 580px;
    display: flex; align-items: center; gap: 8px;
    font-family: "Audiowide", sans-serif; font-size: 15px;
    color: var(--label-cyan);
  }
  .label-mark .label-square {
    width: 44px; height: 44px; background: var(--label-cyan);
    border: 3px solid var(--label-ink);
  }
</style>
</head>
<body>
  <main class="cover">
    <div class="frame-lines"></div>
    <div class="club-scene" role="img" aria-label="Nightclub under spotlights: a mirrored disco ball, a dancer in pink and a silhouetted crowd on a lit dance floor">
      <div class="light-beams"></div>
      <div class="disco-ball"></div>
      <div class="dancer"></div>
      <div class="crowd"></div>
      <div class="dance-floor"></div>
    </div>
    <h1 class="band-name">GlowPavlane</h1>
    <h2 class="release-title">Keep Turning Round</h2>
    <span class="release-format">EP</span>
    <svg class="facet-shape" viewBox="0 0 180 150" role="img" aria-label="Faceted cyan decorative shape">
      <polygon points="20,45 125,0 180,20 180,150 0,150" fill="#2aa6c9"/>
    </svg>
    <div class="label-mark"><span class="label-square"></span><span>Brightmoor Platter</span></div>
  </main>
</body>
</html>
```